New design for Vel Hart [Plonix]

I manage a small web hosting company that I have been doing for many years, and I have quite a few clients that have been with me for a long time. A lot of them have extremely outdated websites such as the one this project is for " www.velhart.com.au ". I am transferring all my clients over to Plonix white-label. The website is very basic, it's only a small amount of links and a contact form.
I need a design that is up-to-date and attractive for today's standards, and of course plonix compatible.
Thanks
Industry/Entity Type
It Company
Look and feel
Each slider illustrates characteristics of the customer's brand and the style your logo design should communicate.

```html
<!DOCTYPE html>
<html lang="en">
<head>
<meta charset="utf-8">
<title>Vel Hart – The Generator Service Specialists</title>
<link href="https://fonts.googleapis.com/css2?family=Arimo:wght@400;700&family=Open+Sans:ital,wght@0,400;0,700;1,400&display=swap" rel="stylesheet">
<style>
  :root {
    --page-light: #efefef;
    --page-blue: #0b4c8c;
    --nav-top: #1c63ad;
    --nav-bottom: #053468;
    --nav-active: #bb2a0e;
    --nav-divider: #0a3f78;
    --ink: #111111;
    --heading-blue: #0c2f6b;
    --white: #ffffff;
    --panel-top: #f4f4f4;
    --panel-bottom: #e6e6e6;
    --panel-border: #c8c8c8;
    --rule: #d6d6d6;
    --bullet: #0c2f6b;
    --footer-bg: #363636;
    --footer-text: #f0f0f0;
  }
  * { box-sizing: border-box; margin: 0; padding: 0; }
  html, body { width: 1083px; height: 1200px; overflow: hidden; }
  body {
    position: relative;
    font-family: "Arimo", Arial, sans-serif;
    color: var(--ink);
    background: linear-gradient(to bottom, var(--page-light) 0, var(--page-light) 294px, var(--page-blue) 294px);
  }
  .site-header { position: absolute; left: 32px; top: 0; width: 1019px; height: 123px; }
  .brand {
    position: absolute; left: 12px; top: 40px;
    display: flex; align-items: center; gap: 10px;
    font-family: "Open Sans", sans-serif; font-weight: 700; font-size: 34px;
    color: var(--nav-active);
  }
  .brand-dot { width: 22px; height: 22px; border-radius: 50%; background: var(--heading-blue); }
  .call { position: absolute; right: 0; top: 33px; text-align: right; color: var(--heading-blue); }
  .call-label { font-size: 18px; }
  .call-number { display: flex; align-items: center; gap: 8px; font-size: 28px; margin-top: 4px; }
  .main-nav {
    position: absolute; left: 32px; top: 123px; width: 1019px; height: 47px;
    background: linear-gradient(to bottom, var(--nav-top), var(--nav-bottom));
    border-radius: 4px 4px 0 0; display: flex; overflow: hidden;
  }
  .main-nav a {
    color: var(--white); text-decoration: none; font-size: 15.5px;
    display: flex; align-items: center; justify-content: center;
    border-right: 1px solid var(--nav-divider);
  }
  .main-nav a.active { background: var(--nav-active); }
  .hero {
    position: absolute; left: 32px; top: 170px; width: 1019px; height: 319px;
    background: linear-gradient(100deg, #5d6459 0%, #b38a2e 30%, #d7ac45 50%, #a8843a 70%, #c9c9c4 100%);
  }
  .content { position: absolute; left: 32px; top: 489px; width: 1019px; height: 499px; background: var(--white); }
  .welcome { position: absolute; left: 54px; top: 32px; width: 530px; }
  .welcome h1 { font-family: "Open Sans", sans-serif; font-weight: 400; font-size: 27px; color: var(--heading-blue); line-height: 1.1; }
  .welcome h1 strong { font-weight: 700; }
  .tagline { font-family: "Open Sans", sans-serif; font-style: italic; font-size: 17.5px; color: var(--heading-blue); margin-top: 2px; }
  .welcome p.body { font-size: 15px; line-height: 17.6px; margin-top: 16px; }
  .services-panel {
    position: absolute; left: 648px; top: 25px; width: 341px; height: 425px;
    border: 1px solid var(--panel-border); border-radius: 5px;
    background: linear-gradient(to bottom, var(--panel-top), var(--panel-bottom));
  }
  .services-panel h2 {
    height: 42px; padding-left: 20px; line-height: 42px;
    font-family: "Open Sans", sans-serif; font-weight: 400; font-size: 21px; color: #222;
    border-bottom: 1px solid var(--panel-border);
    background: linear-gradient(to bottom, #f7f7f7, #dedede); border-radius: 5px 5px 0 0;
  }
  .services-photo {
    margin: 10px 0 0 8px; width: 323px; height: 111px;
    background: linear-gradient(120deg, #9fb8cf, #c9d3da 50%, #8f9aa3);
    border: 2px solid #fff; box-shadow: 0 0 2px #999;
  }
  .services-list { list-style: none; margin: 22px 0 0 37px; width: 266px; }
  .services-list li {
    height: 32px; display: flex; align-items: center; gap: 11px;
    font-size: 15px; border-bottom: 1px solid var(--rule); padding-left: 8px;
  }
  .services-list li:last-child { border-bottom: none; }
  .services-list li::before { content: ""; width: 7px; height: 7px; border-radius: 50%; background: var(--bullet); }
  .site-footer {
    position: absolute; left: 32px; top: 988px; width: 1019px; height: 181px;
    background: var(--footer-bg); border-top: 2px solid var(--page-blue);
    color: var(--footer-text); font-size: 12.5px; line-height: 17px;
  }
  .footer-col { position: absolute; top: 14px; }
  .footer-col h3 { font-size: 12.5px; font-weight: 700; }
  .footer-col h3 + h3, .footer-col ul + h3 { margin-top: 8px; }
  .footer-col ul { list-style: none; }
  .copyright { position: absolute; right: 22px; top: 14px; }
</style>
</head>
<body>
  <header class="site-header">
    <div class="brand"><span>Vel Hart</span><span class="brand-dot"></span></div>
    <div class="call">
      <div class="call-label">Call Us:</div>
      <div class="call-number">
        <svg width="30" height="30" viewBox="0 0 30 30" aria-hidden="true">
          <circle cx="15" cy="15" r="13.5" fill="none" stroke="#0c2f6b" stroke-width="2"/>
          <path d="M10.5 8.5c1-.6 1.8-.4 2.4.6l1 1.8c.4.8.2 1.5-.5 2l-.7.5c.6 1.6 1.8 3 3.4 3.7l.6-.7c.5-.6 1.2-.8 2-.4l1.8 1c1 .6 1.1 1.4.5 2.3-1 1.4-2.4 2-4.2 1.3-3.6-1.4-6.3-4.2-7.4-7.8-.5-1.8.1-3.3 1.1-4.3z" fill="#0c2f6b"/>
        </svg>
        <span>(03) 9000 4821</span>
      </div>
    </div>
  </header>

  <nav class="main-nav">
    <a class="active" href="#" style="width:80px">Home</a>
    <a href="#" style="width:98px">About Us</a>
    <a href="#" style="width:170px">Products &amp; Services</a>
    <a href="#" style="width:153px">Projects &amp; Clients</a>
    <a href="#" style="width:118px">What's New</a>
    <a href="#" style="width:110px">Contact Us</a>
  </nav>

  <div class="hero" role="img" aria-label="Row of large yellow diesel generator sets in an engine room"></div>

  <main class="content">
    <section class="welcome">
      <h1>Welcome to <strong>Vel Hart</strong></h1>
      <p class="tagline">The Generator Service Specialists - Tarrock Summit Dealer</p>
      <p class="body">Vel Hart, a Company dedicated to offering superior customer service, believes that a generator set installation is not only an engine but a complete system, covering fuel systems (gas &amp; diesel); exhaust systems; controls; switchboards; building interfaces; cooling systems; starting systems; etc.<br>Vel Hart understands customer's and their systems service requirements for Tarrock, Corbell, RJ Madden and most other brands of generator sets. Vel Hart also conducts and monitors Oil Sampling. This gives a window into the engincs internal condition and assists in extending or determining oil change intervals, overhauls etc.</p>
      <p class="body">Vel Hart aims to provide to customers a total (one stop shop) solution.</p>
      <p class="body">Vel Hart has the personnel and equipment to offer these services without having to outsource.</p>
    </section>

    <aside class="services-panel">
      <h2>Products &amp; Services</h2>
      <div class="services-photo" role="img" aria-label="Service technician in a hard hat at an industrial plant"></div>
      <ul class="services-list">
        <li>Generator Sets</li>
        <li>Services &amp; Contracts</li>
        <li>Controls &amp; PLC's</li>
        <li>Batteries &amp; Chargers</li>
        <li>Upgrades</li>
        <li>Acoustic Enclosures</li>
        <li>Installation</li>
      </ul>
    </aside>
  </main>

  <footer class="site-footer">
    <div class="footer-col" style="left:21px">
      <h3>Home</h3>
      <h3>About Us</h3>
      <ul><li>Company History</li><li>Company Philosophy</li><li>Company Management</li></ul>
    </div>
    <div class="footer-col" style="left:189px">
      <h3>Products &amp; Services</h3>
      <ul><li>Generator Sets</li><li>Services &amp; Contracts</li><li>Controls &amp; PLC's</li><li>Batteries &amp; Chargers</li><li>Upgrades</li><li>Acoustic Enclosures</li><li>Installation</li></ul>
    </div>
    <div class="footer-col" style="left:382px">
      <h3>Projects &amp; Clients</h3>
      <ul><li>Current Projects</li><li>Completed Projects</li><li>Clients &amp; References</li></ul>
    </div>
    <div class="footer-col" style="left:573px">
      <h3>Contact Us</h3>
      <h3>What's New</h3>
      <ul><li>Products</li><li>Used Equipment</li></ul>
    </div>
    <div class="copyright">Copyright ©2011 Vel Hart</div>
  </footer>
</body>
</html>
```